New Website for Consulting Company

Our company needs a fresh web design to help us drive our business forward. We are a consulting and software provider to Airports, Air Traffic Organizations, Builders and Architects. We specialize in analyzing operations, monitoring noise levels and creating software to improve operations, meet customer requirements and improve public relations.
Additional Info:
- Additional requirements can be found in the Web Design Brief
- Logo and logo branding attached
Target Market(s)
Airlines, Airports, Government Agencies, and Real Estate Developers
Industry/Entity Type
Aviation
Coding
Coded - Design and coding required
Number of Pages Required
2 page
Colors
Designer to choose colors to be used in the design.
Requirements
Must have
- - Create a Wordpress Design (Coded - Design and coding required)
- - Designer must provide full implementation/coding depending on the platform chosen by the client (i.e. Wordpress theme, HTML/CSS, etc.)
- - This is a multi-page site; Supporting pages can be formatted the same, but links need to be in place
- - Colors used must be grey scale, black or match the logo. It is not necessary to use all the colors in our logo
Should not have
- We are not looking for an overly bright site. While our logo has 5 different colors, it is not necessary to use all of them.

```html
<!DOCTYPE html>
<html lang="en">
<head>
<meta charset="utf-8">
<title>Skylane Analytics – Aviation, Technology &amp; Visualized</title>
<link rel="stylesheet" href="https://fonts.googleapis.com/css2?family=Roboto:wght@300;400;500;700&display=swap">
<style>
:root{
  --blue:#2f8fd8;
  --blue-footer:#3d8ed3;
  --green:#6cbf3f;
  --ink:#2d3035;
  --text:#555a60;
  --muted:#8a9096;
  --grey-band:#e5e6e8;
  --experts-bg:#eef0f4;
  --card-inner:#eceef1;
  --bottom:#2c2e32;
  --white:#ffffff;
}
*{box-sizing:border-box;margin:0;padding:0}
html,body{width:1200px;height:3103px;overflow:hidden}
body{font-family:"Roboto",Arial,sans-serif;color:var(--text);background:var(--white);position:relative}
.abs{position:absolute}

/* hero */
.hero{top:0;left:0;width:1200px;height:604px;background:linear-gradient(135deg,#3b4552 0%,#2a323c 45%,#46505c 75%,#2b3139 100%)}
.hero-photo{position:absolute;inset:0;background:radial-gradient(ellipse at 30% 40%,rgba(120,130,140,.45),transparent 60%),radial-gradient(ellipse at 80% 30%,rgba(90,110,130,.4),transparent 55%)}
.brand{position:absolute;left:68px;top:58px;display:flex;align-items:center;gap:10px;color:var(--white);font-weight:700;font-size:34px;letter-spacing:-.5px}
.brand-dot{width:14px;height:14px;border-radius:50%;background:var(--blue)}
.nav{position:absolute;top:76px;right:64px;display:flex;gap:30px;font-size:11.5px;font-weight:500;color:var(--white)}
.nav a{color:inherit;text-decoration:none;padding-bottom:6px}
.nav a.active{border-bottom:2px solid var(--white)}
.hero-title{position:absolute;top:238px;left:0;width:1200px;text-align:center;color:var(--white);font-weight:400;font-size:60px;line-height:68px}
.hero-title .accent{color:var(--blue)}
.btn{display:flex;align-items:center;justify-content:center;gap:14px;background:var(--green);color:var(--white);font-size:15px;font-weight:500;text-decoration:none}
.hero .btn{position:absolute;left:497px;top:434px;width:206px;height:46px}

/* what we do */
.what{top:604px;left:0;width:470px;height:602px;background:linear-gradient(160deg,#5b6470 0%,#8a929c 45%,#4d5560 100%)}
.what-copy{position:absolute;left:0;top:208px;width:470px;text-align:center;color:var(--white)}
.section-title{font-size:22px;font-weight:400;color:var(--blue);text-transform:uppercase}
.rule{width:42px;height:3px;background:var(--blue);margin:10px auto 0}
.what-copy p{margin:16px auto 0;width:370px;font-size:14.5px;line-height:25px}
.services{top:604px;left:470px;width:730px;height:602px;background:var(--grey-band)}
.service{position:absolute;width:347px;height:286px;background:var(--white);text-align:center}
.service svg{display:block;margin:38px auto 0}
.service h3{margin-top:14px;font-size:17px;font-weight:400;color:var(--blue)}
.service .rule{width:44px;height:2px;margin-top:6px}
.service p{width:270px;margin:12px auto 0;font-size:11.5px;line-height:21px;color:var(--ink)}

/* products */
.products{top:1206px;left:0;width:1200px;height:408px}
.centered{text-align:center}
.products .section-title{margin-top:48px}
.lead{margin:26px auto 0;width:800px;font-size:15px;line-height:22px;color:var(--ink)}
.product-logo{position:absolute;left:134px;top:197px;width:267px;height:134px;border:1px solid #d8dbe0;display:flex;align-items:center;justify-content:center;font-size:34px;font-weight:400;color:#8ca0b8;letter-spacing:1px}
.product-text{position:absolute;left:441px;top:218px;width:625px;color:var(--ink)}
.product-text h4{font-size:15px;font-weight:400;margin-bottom:6px}
.product-text p{font-size:11.5px;line-height:16px}

/* experts */
.experts{top:1614px;left:0;width:1200px;height:575px;background:var(--experts-bg)}
.experts .section-title{margin-top:40px}
.expert-card{position:absolute;left:137px;top:105px;width:926px;height:400px;background:var(--white)}
.expert-inner{position:absolute;left:12px;top:14px;width:902px;height:370px;background:var(--card-inner)}
.expert-photo{position:absolute;left:58px;top:0;width:341px;height:370px;background:linear-gradient(180deg,#d9dde2 0%,#b8bec6 50%,#3a3f48 100%)}
.expert-info{position:absolute;left:441px;top:62px;width:430px;color:var(--ink)}
.expert-info h4{font-size:19px;font-weight:400}
.expert-info .role{font-size:14px;margin-top:10px}
.expert-info p{font-size:14.5px;line-height:20px;margin-top:22px}
.arrow{position:absolute;top:274px}

/* join */
.join{top:2189px;left:0;width:1200px;height:532px}
.join-copy{position:absolute;left:120px;top:94px;width:400px}
.join-copy .rule{margin:8px 0 0}
.join-copy p{margin-top:26px;font-size:13.5px;line-height:21px;color:var(--muted)}
.perk{position:absolute;top:272px;width:120px;text-align:center;font-size:13.5px;color:var(--ink)}
.perk svg{display:block;margin:0 auto 10px}
.join .btn{position:absolute;left:221px;top:393px;width:182px;height:50px}
.video{position:absolute;left:573px;top:97px;width:528px;height:346px;background:linear-gradient(120deg,#c8ccd0 0%,#8e959d 45%,#d7d9db 100%)}
.video svg{position:absolute;left:228px;top:137px}

/* footer */
.footer{top:2721px;left:0;width:1200px;height:296px;background:var(--blue-footer);color:var(--white)}
.footer-col{position:absolute;top:40px;font-size:13.5px;line-height:17px}
.footer-col h5{font-size:13.5px;font-weight:400;text-transform:uppercase;margin-bottom:6px}
.footer-col .gap{margin-top:20px}
.tweet{font-size:11.5px;line-height:15px;margin-bottom:14px}
.divider{position:absolute;top:40px;width:1px;height:220px;background:rgba(255,255,255,.25)}
.field{width:258px;height:34px;border:2px solid var(--white);margin-bottom:14px;font-size:11px;padding:10px 8px;text-transform:uppercase}
.footer .btn{width:126px;height:38px;font-size:13px}
.bottom{top:3017px;left:0;width:1200px;height:86px;background:var(--bottom);color:var(--white);text-align:center;font-size:12.5px;line-height:17px;padding-top:24px}
</style>
</head>
<body>

<header class="abs hero">
  <div class="hero-photo" role="img" aria-label="Team reviewing printed charts and reports on a desk"></div>
  <div class="brand"><span class="brand-dot"></span>Skylane Analytics</div>
  <nav class="nav">
    <a class="active" href="#">Home</a><a href="#">Airports</a><a href="#">Airspace</a><a href="#">Emissions</a><a href="#">Acoustics</a><a href="#">Visualizaton</a><a href="#">About</a><a href="#">Contact</a>
  </nav>
  <h1 class="hero-title">AVIATION, TECHNOLOGY<br>&amp; <span class="accent">VISUALIZED</span></h1>
  <a class="btn" href="#">GET IN TOUCH</a>
</header>

<section class="abs what" role="img" aria-label="Business colleagues shaking hands at a meeting table">
  <div class="what-copy">
    <h2 class="section-title">What we do</h2>
    <div class="rule"></div>
    <p>Skylane Analytics invents and deploys innovative management and technology solutions that address complex noise and airspace issues for airports and residential communities.</p>
  </div>
</section>

<section class="abs services">
  <div class="service" style="left:8px;top:8px">
    <svg width="76" height="76" viewBox="0 0 76 76" fill="none" stroke="#2f8fd8" stroke-width="2.5"><circle cx="38" cy="38" r="35"/><path d="M49 30a14 14 0 1 0 2 12"/><path d="M50 22v9h-9"/></svg>
    <h3>AVIATION</h3><div class="rule"></div>
    <p>Lorem Ipsum is simply dummy text of the printing and typesetting industry. Lorem Ipsum has been the industry's standard dummy text ever</p>
  </div>
  <div class="service" style="left:364px;top:8px">
    <svg width="76" height="76" viewBox="0 0 76 76" fill="none" stroke="#2f8fd8" stroke-width="2.5"><circle cx="38" cy="38" r="35"/><rect x="26" y="22" width="24" height="32" rx="2"/><path d="M33 20h10v5H33zM30 32l2 2 3-3M38 33h8M30 40l2 2 3-3M38 41h8M30 48h16"/></svg>
    <h3>VISUALIZED</h3><div class="rule"></div>
    <p>Lorem Ipsum is simply dummy text of the printing and typesetting industry. Lorem Ipsum has been the industry's standard dummy text ever since the</p>
  </div>
  <div class="service" style="left:8px;top:304px">
    <svg width="76" height="76" viewBox="0 0 76 76" fill="none" stroke="#2f8fd8" stroke-width="2.5"><circle cx="38" cy="38" r="35"/><circle cx="38" cy="36" r="15"/><path d="M23 36h30M38 21c-8 8-8 22 0 30M38 21c8 8 8 22 0 30M26 28h24M26 44h24M30 56h16"/></svg>
    <h3>TECHNOLOGY</h3><div class="rule"></div>
    <p>Lorem Ipsum is simply dummy text of the printing and typesetting industry. Lorem Ipsum has been the industry's standard dummy text ever since the</p>
  </div>
  <div class="service" style="left:364px;top:304px">
    <svg width="76" height="76" viewBox="0 0 76 76" fill="none" stroke="#2f8fd8" stroke-width="2.5"><circle cx="38" cy="38" r="35"/><path d="M22 54h32M26 52v-8M33 52v-13M40 52v-9M47 52v-17M24 40l9-8 7 5 11-12M46 25h5v5"/></svg>
    <h3>EMISSIONS</h3><div class="rule"></div>
    <p>Lorem Ipsum is simply dummy text of the printing and typesetting industry. Lorem Ipsum has been the industry's standard dummy text ever since the</p>
  </div>
</section>

<section class="abs products">
  <div class="centered">
    <h2 class="section-title">Our Products</h2>
    <div class="rule"></div>
    <p class="lead">Sed ut perspiciatis unde omnis iste natus error sit voluptatem accusantium doloremque laudantium, totam rem aperiam, eaque ipsa quae ab illo inventore</p>
  </div>
  <div class="product-logo">AEROVIEW</div>
  <div class="product-text">
    <h4>AEROVIEW wins 2012 software innovation!!</h4>
    <p>AEROVIEW is a web-based application designed to create, evaluate and display flight operations in 3D. This software tool evaluates the acoustic and environmental impacts from new Performance Based Procedures as well as new runways and airfield configurations, providing a display of noise impacts using various acoustic parameters including A-weighted noise levels and audibility detection. AEROVIEW can be used for all classes of aircraft operations ranging from commercial jets on a single runway to metroplex operations.</p>
  </div>
</section>

<section class="abs experts">
  <div class="centered">
    <h2 class="section-title">Our Experts</h2>
    <div class="rule"></div>
  </div>
  <svg class="arrow" style="left:80px" width="22" height="40" viewBox="0 0 22 40" fill="none" stroke="#2f8fd8" stroke-width="3"><path d="M19 2L3 20l16 18"/></svg>
  <svg class="arrow" style="left:1097px" width="22" height="40" viewBox="0 0 22 40" fill="none" stroke="#2f8fd8" stroke-width="3"><path d="M3 2l16 18L3 38"/></svg>
  <div class="expert-card">
    <div class="expert-inner">
      <div class="expert-photo" role="img" aria-label="Portrait of the chief executive officer in a dark suit"></div>
      <div class="expert-info">
        <h4>Daniel</h4>
        <div class="role">Chief Executive Officer</div>
        <p>Sed ut perspiciatis unde omnis iste natus error sit voluptatem accusantium doloremque laudantium, totam rem aperiam, eaque ipsa quae ab illo inventore</p>
        <p>Sed ut perspiciatis unde omnis iste natus error sit voluptatem accusantium doloremque laudantium, totam rem aperiam, eaque ipsa quae ab illo inventore</p>
      </div>
    </div>
  </div>
</section>

<section class="abs join">
  <div class="join-copy">
    <h2 class="section-title">Join Us</h2>
    <div class="rule"></div>
    <p>Sed ut perspiciatis unde omnis iste natus error sit voluptatem accusantium doloremque laudantium, totam rem aperiam, eaque ipsa quae ab illo inventore. Sed ut perspiciatis unde omnis iste natus error sit voluptatem accusantium doloremque.</p>
  </div>
  <div class="perk" style="left:108px">
    <svg width="54" height="54" viewBox="0 0 54 54" fill="none" stroke="#2f8fd8" stroke-width="2"><circle cx="27" cy="27" r="25"/><circle cx="27" cy="27" r="12"/><path d="M21 27l4 4 8-8"/></svg>MEANINGFUL</div>
  <div class="perk" style="left:232px">
    <svg width="54" height="54" viewBox="0 0 54 54" fill="none" stroke="#2f8fd8" stroke-width="2"><circle cx="27" cy="27" r="25"/><circle cx="27" cy="23" r="8"/><path d="M23 31v6h8v-6M24 40h6"/></svg>REWARDING</div>
  <div class="perk" style="left:337px">
    <svg width="54" height="54" viewBox="0 0 54 54" fill="none" stroke="#2f8fd8" stroke-width="2"><circle cx="27" cy="27" r="25"/><rect x="17" y="17" width="20" height="20"/><circle cx="17" cy="17" r="3" fill="#fff"/><circle cx="37" cy="17" r="3" fill="#fff"/><circle cx="17" cy="37" r="3" fill="#fff"/><circle cx="37" cy="37" r="3" fill="#fff"/></svg>FLEXIBLE</div>
  <div class="perk" style="left:430px">
    <svg width="54" height="54" viewBox="0 0 54 54" fill="none" stroke="#2f8fd8" stroke-width="2"><circle cx="27" cy="27" r="25"/><path d="M17 16h20L27 29zM27 29v11M21 40h12M34 12l-4 8"/></svg>FUN</div>
  <a class="btn" href="#">EXPLORE
    <svg width="26" height="14" viewBox="0 0 26 14" fill="none" stroke="#fff" stroke-width="2"><path d="M0 7h24M18 1l6 6-6 6"/></svg></a>
  <div class="video" role="img" aria-label="Video still of colleagues discussing work around a table">
    <svg width="72" height="72" viewBox="0 0 72 72" fill="none"><circle cx="36" cy="36" r="33" stroke="#fff" stroke-width="3"/><path d="M29 24l20 12-20 12z" fill="#fff"/></svg>
  </div>
</section>

<footer class="abs footer">
  <div class="footer-col" style="left:64px">
    Address:<br>Skylane Analytics<br>4180 Harbor Crest Drive, Suite 310<br>Bayview, California 90412
    <div class="gap">Phone: +1 (555) 410-2280</div>
    <div class="gap">Fax: +1 (555) 410-2285</div>
    <div class="gap">hello@skylaneanalytics.example</div>
  </div>
  <div class="divider" style="left:341px"></div>
  <div class="footer-col" style="left:414px;width:340px">
    <h5>Follow us on Twitter</h5>
    <div class="tweet">Lakeport aims for new control tower | The Riverbend Courier<br>https://lnk.example/a7Qx2<br>about 19 hours ago</div>
    <div class="tweet">Millbrook Regional Airport Air Traffic Control Tower Recognized by Regional Airfield Council<br>https://lnk.example/k9Tm4<br>06:15 PM Jun 27th</div>
  </div>
  <div class="divider" style="left:776px"></div>
  <div class="footer-col" style="left:869px">
    <h5>Contact us now</h5>
    <div class="field">Name</div>
    <div class="field">Phone</div>
    <div class="field">Email</div>
    <a class="btn" href="#">SUBMIT
      <svg width="22" height="12" viewBox="0 0 22 12" fill="none" stroke="#fff" stroke-width="2"><path d="M0 6h20M15 1l5 5-5 5"/></svg></a>
  </div>
</footer>

<div class="abs bottom">
  ©2010 Skylane Analytics. All Rights Reserved.<br>
  Home | Airports | Airspace | Emissions | Acoustics | Visualization | About | Contact
</div>

</body>
</html>
```